Korvane Sky Works, LLC - Business Card

I currently have a drone business that specializes in aerial photography, thermal image inspections, deer recovery, search and rescue, custom agricultural applications. i will attach my current business card as well as some logos to incorporate for a new up to date business card
Updates

Designs look the same

Sick

Target Market(s)

farmers, hunters

Contact Information for Business Card

name address phone number (as existing card i attached)

Requirements
Must have
• im good with existing business card, but would like an agricultural twist

```html
<!DOCTYPE html>
<html lang="en">
<head>
<meta charset="utf-8">
<title>Korvane Sky Works, LLC – Business Card</title>
<link href="https://fonts.googleapis.com/css2?family=Poppins:wght@400;500;600;700&family=Roboto:wght@400;500&display=swap" rel="stylesheet">
<style>
  :root{
    --backdrop:#2b2b2b;
    --green:#2f9a2a;
    --green-dark:#0f5e1c;
    --green-deep:#0b4a15;
    --green-light:#5cc23a;
    --ink:#1d1d1d;
    --band:#1c1c1c;
    --paper:#f7f7f5;
    --muted:#6b6b6b;
    --white:#ffffff;
  }
  *{box-sizing:border-box;margin:0;padding:0}
  html,body{width:1200px;height:852px;overflow:hidden}
  body{background:var(--backdrop);font-family:"Poppins",sans-serif;position:relative}

  .card{position:absolute;top:283px;width:500px;height:286px;border-radius:18px;overflow:hidden}
  .card--front{left:70px;background:var(--green-dark)}
  .card--back{left:630px;background:var(--paper)}

  /* front */
  .front__aerial{position:absolute;inset:0;background:linear-gradient(135deg,#1f8a2c 0%,#137227 45%,#0c5a1a 100%)}
  .front__mark{position:absolute;left:0;right:0;top:58px;display:flex;align-items:center;justify-content:center;gap:12px}
  .front__dot{width:26px;height:26px;border-radius:50%;background:var(--green-light)}
  .front__name{font-family:"Poppins",sans-serif;font-weight:700;font-size:38px;letter-spacing:2px;color:var(--white)}
  .front__band{position:absolute;left:0;right:0;top:196px;height:58px;background:var(--band);display:flex;flex-direction:column;align-items:center;justify-content:center;gap:2px}
  .front__services{font-family:"Roboto",sans-serif;font-size:14px;color:var(--white);letter-spacing:.2px}
  .front__strip{position:absolute;left:0;right:0;top:254px;bottom:0;background:var(--green)}

  /* back */
  .back__brand{position:absolute;left:34px;top:34px;display:flex;align-items:center;gap:10px}
  .back__brand-dot{width:18px;height:18px;border-radius:50%;background:var(--green)}
  .back__brand-name{font-weight:700;font-size:26px;color:var(--ink);letter-spacing:1px}
  .services{position:absolute;left:40px;top:104px;list-style:none}
  .services li{font-weight:600;font-size:15px;color:var(--ink);line-height:27px}
  .services li::before{content:"»";color:var(--green);font-weight:700;margin-right:8px}
  .person{position:absolute;left:275px;top:30px}
  .person__name{font-weight:700;font-size:21px;color:var(--green);letter-spacing:.5px}
  .person__role{font-size:12px;color:var(--muted);margin-top:-2px}
  .contacts{position:absolute;left:275px;top:96px;list-style:none}
  .contacts li{display:flex;align-items:center;gap:9px;font-family:"Roboto",sans-serif;font-size:13px;color:var(--ink);height:26px}
  .contacts svg{width:18px;height:18px;flex:none}
  .contacts .address{padding-left:27px}
  .back__trim{position:absolute;left:0;bottom:0;width:500px;height:90px}
</style>
</head>
<body>

<section class="card card--front" aria-label="Card front">
  <div class="front__aerial" role="img" aria-label="Aerial photograph of green farmland"></div>
  <div class="front__mark">
    <span class="front__dot"></span>
    <span class="front__name">KORVANE</span>
  </div>
  <div class="front__band">
    <p class="front__services">Thermal Image Inspections &nbsp;|&nbsp; Deer Recovery &nbsp;|&nbsp; Search &amp; Rescue</p>
    <p class="front__services">Real Estate Photography</p>
  </div>
  <div class="front__strip"></div>
</section>

<section class="card card--back" aria-label="Card back">
  <div class="back__brand">
    <span class="back__brand-dot"></span>
    <span class="back__brand-name">KORVANE</span>
  </div>

  <ul class="services">
    <li>Thermal Image Inspections</li>
    <li>Deer Recovery</li>
    <li>Search &amp; Rescue</li>
    <li>Real Estate Photography</li>
  </ul>

  <div class="person">
    <h1 class="person__name">DAWSON HALE</h1>
    <p class="person__role">Owner</p>
  </div>

  <ul class="contacts">
    <li>
      <svg viewBox="0 0 18 18" aria-hidden="true"><circle cx="9" cy="9" r="8" fill="none" stroke="var(--green)" stroke-width="1.4"/><path d="M6.3 5.2l1.4-.3.8 2-.9.7c.4.9 1.1 1.6 2 2l.7-.9 2 .8-.3 1.4c-3 .3-6-2.7-5.7-5.7z" fill="var(--green)"/></svg>
      419-555-0142
    </li>
    <li>
      <svg viewBox="0 0 18 18" aria-hidden="true"><circle cx="9" cy="9" r="8" fill="var(--green)"/><circle cx="9" cy="9" r="4.2" fill="none" stroke="#fff" stroke-width="1"/><path d="M4.8 9h8.4M9 4.8v8.4" stroke="#fff" stroke-width="1"/></svg>
      www.korvaneskyworks.com
    </li>
    <li>
      <svg viewBox="0 0 18 18" aria-hidden="true"><circle cx="9" cy="9" r="8" fill="var(--green)"/><rect x="5" y="6.2" width="8" height="5.6" rx=".6" fill="none" stroke="#fff" stroke-width="1"/><path d="M5.2 6.5L9 9.4l3.8-2.9" fill="none" stroke="#fff" stroke-width="1"/></svg>
      korvaneskyworks@mail.com
    </li>
    <li class="address">214 W. Elm St. Ashford, OH 45890</li>
  </ul>

  <svg class="back__trim" viewBox="0 0 500 90" aria-hidden="true">
    <polygon points="0,72 500,40 500,90 0,90" fill="var(--green)"/>
    <polygon points="0,80 500,56 500,90 0,90" fill="var(--green-deep)" opacity=".55"/>
    <polygon points="300,60 330,58 322,28 292,30" fill="var(--green)"/>
    <polygon points="340,57 372,55 364,16 332,18" fill="var(--green-light)"/>
    <polygon points="384,54 414,52 406,8 376,10" fill="var(--band)"/>
    <polygon points="426,51 500,46 500,0 418,6" fill="var(--band)"/>
  </svg>
</section>

</body>
</html>
```